Real Estate Agent needs business card design

We have logo designed already, want to have business card designed. Very interested in those smaller size business card as they look very trendy. Business name is called TOVANE REALTY

Industry/Entity Type

Business

```html
<!DOCTYPE html>
<html lang="en">
<head>
<meta charset="utf-8">
<title>Tovane Realty – Business Card</title>
<link rel="stylesheet" href="https://fonts.googleapis.com/css2?family=EB+Garamond:wght@400;600&display=swap">
<style>
  :root {
    --backdrop: #e4e4e4;
    --card-black: #050505;
    --panel-charcoal: #161616;
    --gold: #c99a1e;
    --gold-light: #e6bb3c;
    --gold-deep: #a87c10;
    --paper: #f4f3ef;
    --ink: #141414;
  }
  * { margin: 0; padding: 0; box-sizing: border-box; }
  html, body {
    width: 1200px;
    height: 828px;
    overflow: hidden;
    background: var(--backdrop);
  }
  .canvas {
    position: relative;
    width: 1200px;
    height: 828px;
  }
  .card {
    position: absolute;
    top: 197px;
    width: 433px;
    height: 435px;
  }
  /* Front */
  .card-front {
    left: 110px;
    background: var(--card-black);
  }
  .front-frame {
    position: absolute;
    inset: 16px;
    border: 1px solid var(--gold-deep);
    opacity: 0.7;
  }
  .front-panel {
    position: absolute;
    inset: 36px;
    background: var(--panel-charcoal);
  }
  .gold-disc {
    position: absolute;
    left: 58px;
    top: 58px;
    width: 317px;
    height: 317px;
    border-radius: 50%;
    background: radial-gradient(circle at 40% 35%, var(--gold-light) 0%, var(--gold) 55%, var(--gold-deep) 100%);
    display: flex;
    align-items: center;
    justify-content: center;
  }
  .brand-name {
    font-family: "EB Garamond", serif;
    font-weight: 600;
    font-size: 30px;
    letter-spacing: 1px;
    color: var(--ink);
  }
  /* Back */
  .card-back {
    left: 648px;
    background: var(--paper);
    text-align: center;
    font-family: "EB Garamond", serif;
    color: var(--ink);
  }
  .agent-name {
    position: absolute;
    top: 116px;
    width: 100%;
    font-size: 29px;
    font-weight: 400;
    letter-spacing: 0.5px;
  }
  .agent-title {
    position: absolute;
    top: 152px;
    width: 100%;
    font-size: 15px;
    font-weight: 600;
  }
  .gold-rule {
    position: absolute;
    top: 192px;
    left: 186px;
    width: 61px;
    height: 3px;
    background: var(--gold);
  }
  .contact-block {
    position: absolute;
    width: 100%;
    font-size: 18px;
    line-height: 23px;
  }
  .address { top: 217px; }
  .phone-web { top: 289px; }
</style>
</head>
<body>
<main class="canvas">
  <section class="card card-front" aria-label="Card front">
    <div class="front-frame"></div>
    <div class="front-panel"></div>
    <div class="gold-disc">
      <span class="brand-name">TOVANE REALTY</span>
    </div>
  </section>

  <section class="card card-back" aria-label="Card back">
    <h1 class="agent-name">HELENA MARSH</h1>
    <p class="agent-title">Senior Property Consultant</p>
    <div class="gold-rule"></div>
    <p class="contact-block address">7C, 48 Harbour Lane,<br>Kirribilli Heights, NSW 2061</p>
    <p class="contact-block phone-web">0400 517 293<br>www.tovanerealty.com.au</p>
  </section>
</main>
</body>
</html>
```